Radiology Department needs a series of 3 facebook posts - similar design

We need a series of 3 posts for our facebook page, each one presenting the activity of one of 3 physicians.
The main design elements can be the same, the only thing that will change between posts will be the field of activity and name of the physician and the representative image of its activity.
If needed the design elements can be slightly different between posts for better adjustment to the representative images.
You can find as an attachment:
- Manual of institutional identity of the Hospital (Velmor Clinica)
- Our facebook cover page
- Our department video
- The representative images for each post, identified with the name of each physician
- The Institutional identity manual with the logo of "Brisa Medical School" - just for Dr Tomas Brandilo post.
So, each one of the three posts should state the name and field of activity of each physician, including somehow the corresponding representative image, and should have background innovative design elements.
Post 1:
Name of the physician: Prof. Doutor Rui Castelvo
Field of activity: Imagiologia Reumatológica e do Sistema Músculo-Esquelético
Image as an attachment
Post 2:
Name of the physician: Prof.ª Doutora Inês Barroca
Field of activity: Imagiologia Cardíaca
Image as an attachment
Post 3:
Name of the physician: Dr. Tomas Lupo
Field of activity: Tese de Doutoramento em Curso - Identificação da Lesão Cartilagínea Precoce. Com orientação do Prof. Doutor Rui Castelvo e Prof.ª Doutora Inês Sofia Carvalhal.
Image as an attachment
Just for Dr Tomas Lupo, the logo of Brisa Medical School should also be included (please check the corresponding institutional identity manual that was just added in documents).
Updates

Just for Dr Tomas Brandilo, the logo of Brisa Medical School should also be included (please check the corresponding institutional identity manual that was just added in documents).

Please note that we are just looking for 3 facebook POSTS, not facebook cover page, thanks.

Please kindly note that we are looking for facebook POST and NOT facebook cover page.

Target Market(s)

General Population

Industry/Entity Type

Health

Font styles to use
Other font styles liked:
• Check manual of institutional identity and try to approach if appropriate

Requirements
Must have
• Check project description.
Nice to have
• If the designer finds appropriate, the logo of the Hospital would be nice in all the three posts, the most simple one just stating "VelmorClinica" - please check the attached manual of institutional identity

```html
<!DOCTYPE html>
<html lang="pt">
<head>
<meta charset="utf-8">
<title>VelmorClinica – Radiologia – Facebook Posts</title>
<link rel="stylesheet" href="https://fonts.googleapis.com/css2?family=Montserrat:wght@400;500;700;800&display=swap">
<style>
  :root {
    --board: #666666;
    --teal: #00635f;
    --yellow: #fdc600;
    --ink-dark: #2b2b2b;
    --white: #ffffff;
    --badge: #e6e6e6;
  }
  html, body {
    margin: 0;
    padding: 0;
    width: 1200px;
    height: 1200px;
    overflow: hidden;
    background: var(--board);
  }
  .board { display: block; width: 1200px; height: 1200px; }
  .board text { font-family: "Montserrat", Arial, sans-serif; }
  .post-label { fill: var(--white); font-weight: 700; font-size: 26px; text-anchor: middle; }
  .post-paper { fill: url(#paperTone); }
  .brand-mark { fill: var(--teal); }
  .brand-name { fill: var(--teal); font-weight: 700; font-size: 58px; }
  .frame-band { fill: var(--yellow); }
  .physician { fill: var(--teal); font-size: 34px; font-weight: 400; text-anchor: middle; }
  .physician-name { font-weight: 700; }
  .field-title { fill: var(--teal); font-weight: 800; text-anchor: middle; }
  .field-sub { fill: var(--ink-dark); font-weight: 700; font-size: 22px; text-anchor: middle; }
  .footer-band { fill: var(--teal); }
  .footer-text { fill: var(--white); font-weight: 700; text-anchor: middle; }
  .partner-badge { fill: var(--badge); }
  .partner-name { fill: var(--ink-dark); font-weight: 700; text-anchor: middle; }
</style>
</head>
<body>
<svg class="board" viewBox="0 0 1932 1932" xmlns="http://www.w3.org/2000/svg">
  <defs>
    <linearGradient id="paperTone" x1="0" y1="0" x2="1" y2="1">
      <stop offset="0" stop-color="#f4f4f4"/>
      <stop offset="0.5" stop-color="#ffffff"/>
      <stop offset="1" stop-color="#f2f2f2"/>
    </linearGradient>
    <radialGradient id="toneHands" cx="0.5" cy="0.5" r="0.5">
      <stop offset="0" stop-color="#9a9a9a"/>
      <stop offset="0.45" stop-color="#4a4a4a"/>
      <stop offset="1" stop-color="#000000"/>
    </radialGradient>
    <radialGradient id="toneHeart" cx="0.55" cy="0.5" r="0.45">
      <stop offset="0" stop-color="#8a2a22"/>
      <stop offset="0.55" stop-color="#5a1812"/>
      <stop offset="1" stop-color="#000000"/>
    </radialGradient>
    <radialGradient id="toneCartilage" cx="0.5" cy="0.6" r="0.6">
      <stop offset="0" stop-color="#2f5cff"/>
      <stop offset="0.6" stop-color="#1a3fe0"/>
      <stop offset="1" stop-color="#0a1e8c"/>
    </radialGradient>
    <filter id="paperShadow" x="-5%" y="-5%" width="110%" height="110%">
      <feDropShadow dx="0" dy="4" stdDeviation="4" flood-color="#000" flood-opacity="0.35"/>
    </filter>
  </defs>

  <!-- Post 1 -->
  <text class="post-label" x="524" y="68">FB POST-1</text>
  <g class="post post-1" transform="translate(104 101)">
    <rect class="post-paper" width="840" height="841" filter="url(#paperShadow)"/>
    <g class="brand">
      <circle class="brand-mark" cx="240" cy="99" r="48"/>
      <text class="brand-name" x="302" y="120" textLength="342" lengthAdjust="spacingAndGlyphs">VelmorClinica</text>
    </g>
    <rect class="frame-band" x="0" y="234" width="840" height="275"/>
    <rect class="frame-band" x="56" y="188" width="728" height="366" rx="183"/>
    <rect x="76" y="207" width="688" height="329" rx="164.5" fill="url(#toneHands)"
          role="img" aria-label="Angiografia de ambas as mãos em tons de cinzento sobre fundo negro"/>
    <text class="physician" x="420" y="634">Physician: <tspan class="physician-name">Prof. Doutor Rui Castelvo</tspan></text>
    <text class="field-title" x="420" y="685" font-size="44">IMAGIOLOGIA</text>
    <text class="field-title" x="420" y="730" font-size="44">REUMATOLÓGICA E</text>
    <rect class="footer-band" x="0" y="748" width="840" height="70"/>
    <text class="footer-text" x="420" y="793" font-size="24">DO SISTEMA MÚSCULO-ESQUELÉTICO</text>
  </g>

  <!-- Post 2 -->
  <text class="post-label" x="1409" y="68">FB POST-2</text>
  <g class="post post-2" transform="translate(990 101)">
    <rect class="post-paper" width="840" height="841" filter="url(#paperShadow)"/>
    <g class="brand">
      <circle class="brand-mark" cx="240" cy="99" r="48"/>
      <text class="brand-name" x="302" y="120" textLength="342" lengthAdjust="spacingAndGlyphs">VelmorClinica</text>
    </g>
    <rect class="frame-band" x="0" y="234" width="840" height="275"/>
    <rect class="frame-band" x="56" y="188" width="728" height="366" rx="183"/>
    <rect x="76" y="207" width="688" height="329" rx="164.5" fill="url(#toneHeart)"
          role="img" aria-label="Reconstrução 3D do coração com artérias coronárias sobre fundo negro"/>
    <text class="physician" x="420" y="634">Physician: <tspan class="physician-name">Prof.ª Doutora Inês Barroca</tspan></text>
    <text class="field-title" x="420" y="701" font-size="62">IMAGIOLOGIA</text>
    <text class="field-title" x="420" y="765" font-size="62">CARDÍACA</text>
    <rect class="footer-band" x="0" y="771" width="840" height="47"/>
  </g>

  <!-- Post 3 -->
  <g class="post post-3" transform="translate(583 990)">
    <rect class="post-paper" width="840" height="841" filter="url(#paperShadow)"/>
    <g class="brand">
      <circle class="brand-mark" cx="240" cy="76" r="48"/>
      <text class="brand-name" x="302" y="97" textLength="342" lengthAdjust="spacingAndGlyphs">VelmorClinica</text>
    </g>
    <rect class="frame-band" x="0" y="202" width="840" height="276"/>
    <rect class="frame-band" x="56" y="157" width="728" height="365" rx="182.5"/>
    <rect x="76" y="175" width="688" height="330" rx="165" fill="url(#toneCartilage)"
          role="img" aria-label="Mapa de ressonância magnética da cartilagem do joelho em tons de azul com focos vermelhos"/>
    <text class="physician" x="420" y="580">Physician: <tspan class="physician-name">Dr. Tomas Lupo</tspan></text>
    <text class="field-title" x="420" y="627" font-size="44">TESE DE DOUTORAMENTO</text>
    <text class="field-title" x="420" y="671" font-size="44">EM CURSO</text>
    <text class="field-sub" x="420" y="703">IDENTIFICAÇÃO DA LESÃO CARTILAGÍNEA PRECOCE</text>
    <rect class="footer-band" x="0" y="716" width="840" height="47"/>
    <text class="footer-text" x="420" y="737" font-size="15">COM ORIENTAÇÃO DO PROF. DOUTOR RUI CASTELVO</text>
    <text class="footer-text" x="420" y="755" font-size="15">E PROF.ª DOUTORA INÊS SOFIA CARVALHAL</text>
    <rect class="partner-badge" x="300" y="767" width="240" height="48"/>
    <text class="partner-name" x="420" y="797" font-size="17" textLength="216" lengthAdjust="spacingAndGlyphs">BRISA MEDICAL SCHOOL</text>
  </g>
  <text class="post-label" x="1002" y="1884">FB POST-3</text>
</svg>
</body>
</html>
```